NEW STORE PROMOTION FLYER

We need a flyer design for a new lingerie store based in Double Bay.
The people living in Double Bay are most wealthy suburb in Sydney. Our customers are aged at 30+ to 70.
We are offering 'up to 30% off' on selected products.
we recommend using our theme colour: light pink, red, white
the address is:
shop 5/214 Larkmoor Vale Rd, NSW 2049
contact number: 02 8154 3907
We need key information:
1. we want to let neighborhood know that we open a new store.
2. we offer 'up to 30% off' Christmas Sale
3. Please use our theme colour: light pink, red, white
4. Please add the address map on flyer (you may design again if you need )
5.open hour:
Mon - Fri 10:00am - 5:30pm
Sat - Sun 10:00am - 5:30pm
thank you
aged 30+ to 70; they are relatively wealthy.
Store

```html
<!DOCTYPE html>
<html lang="en">
<head>
<meta charset="utf-8">
<title>Velmira Lingerie – New Store Christmas Sale</title>
<link rel="stylesheet" href="https://fonts.googleapis.com/css2?family=Arimo:wght@400;700&family=Gochi+Hand&display=swap">
<style>
  :root {
    --panel-pink: #ebbfe1;
    --damask-pink: #e3a6df;
    --damask-deep: #d48cd3;
    --brand-magenta: #c93ad9;
    --ink: #1c1c1c;
    --map-paper: #fbeef7;
    --map-road: #ffffff;
    --map-line: #d9a3cf;
    --pin-red: #c8202f;
    --photo-dark: #26393c;
    --photo-gold: #b8ad74;
    --photo-skin: #d9b49c;
  }
  html, body {
    margin: 0;
    padding: 0;
    overflow: hidden;
    background: #ffffff;
  }
  .flyer {
    position: relative;
    width: 1200px;
    height: 846px;
    overflow: hidden;
    background: var(--panel-pink);
  }
  .damask-strip {
    position: absolute;
    top: 0;
    width: 120px;
    height: 846px;
    background: linear-gradient(180deg, var(--damask-pink), var(--damask-deep) 50%, var(--damask-pink));
  }
  .damask-strip--left { left: 0; }
  .damask-strip--right { left: 640px; }
  .announcement {
    position: absolute;
    left: 120px;
    top: 0;
    width: 520px;
    height: 846px;
  }
  .brand-name {
    position: absolute;
    left: 0;
    top: 188px;
    width: 520px;
    margin: 0;
    text-align: center;
    font-family: "Gochi Hand", cursive;
    font-weight: 400;
    font-size: 92px;
    line-height: 1;
    color: var(--brand-magenta);
    padding-left: 14px;
    box-sizing: border-box;
  }
  .brand-tagline {
    position: absolute;
    left: 85px;
    top: 304px;
    margin: 0;
    font-family: "Arimo", Arial, sans-serif;
    font-size: 31px;
    letter-spacing: 32px;
    color: var(--ink);
  }
  .opening-message {
    position: absolute;
    left: 0;
    top: 390px;
    width: 516px;
    margin: 0;
    text-align: center;
    font-family: "Arimo", Arial, sans-serif;
    font-size: 24px;
    line-height: 38px;
    color: var(--ink);
  }
  .sale-offer {
    position: absolute;
    left: 14px;
    top: 528px;
    margin: 0;
    white-space: nowrap;
    font-family: "Gochi Hand", cursive;
    color: var(--brand-magenta);
    font-weight: 400;
  }
  .sale-offer__percent {
    font-size: 84px;
    vertical-align: middle;
  }
  .sale-offer__label {
    font-size: 42px;
    margin-left: 36px;
    vertical-align: middle;
  }
  .store-map {
    position: absolute;
    left: 24px;
    top: 660px;
    width: 180px;
    height: 156px;
  }
  .store-details {
    position: absolute;
    left: 226px;
    top: 660px;
    width: 280px;
    font-family: "Arimo", Arial, sans-serif;
    font-size: 14px;
    line-height: 19px;
    color: var(--ink);
  }
  .store-details__block {
    margin: 0 0 8px;
  }
  .store-details__label {
    display: block;
    font-weight: 700;
    color: var(--brand-magenta);
    letter-spacing: 1px;
    text-transform: uppercase;
    font-size: 12px;
  }
  .model-photo {
    position: absolute;
    left: 760px;
    top: 0;
    width: 440px;
    height: 846px;
    background:
      radial-gradient(ellipse 45% 55% at 78% 55%, var(--photo-skin) 0%, rgba(217,180,156,0) 70%),
      linear-gradient(135deg, var(--photo-dark) 0%, var(--photo-gold) 45%, var(--photo-dark) 100%);
  }
</style>
</head>
<body>
  <main class="flyer">
    <div class="damask-strip damask-strip--left" role="img" aria-label="Pink damask wallpaper pattern"></div>

    <section class="announcement">
      <h1 class="brand-name">Velmira</h1>
      <p class="brand-tagline">Lingerie</p>
      <p class="opening-message">are pleased to<br>announce the opening<br>of their new store with a</p>
      <p class="sale-offer"><span class="sale-offer__percent">30%</span><span class="sale-offer__label">off christmas sale</span></p>

      <svg class="store-map" viewBox="0 0 180 156" role="img" aria-label="Street map showing the store on Larkmoor Vale Rd">
        <rect x="0.5" y="0.5" width="179" height="155" rx="6" fill="var(--map-paper)" stroke="var(--map-line)"/>
        <path d="M0 96 L180 70" stroke="var(--map-line)" stroke-width="16"/>
        <path d="M0 96 L180 70" stroke="var(--map-road)" stroke-width="12"/>
        <path d="M62 0 L78 156" stroke="var(--map-road)" stroke-width="8"/>
        <path d="M132 0 L140 156" stroke="var(--map-road)" stroke-width="6"/>
        <path d="M0 30 L62 24" stroke="var(--map-road)" stroke-width="5"/>
        <text x="92" y="98" font-family="Arimo, Arial, sans-serif" font-size="10" fill="var(--ink)" transform="rotate(-8 92 98)">Larkmoor Vale Rd</text>
        <path d="M104 38 c-9 0 -15 7 -15 15 c0 11 15 25 15 25 s15 -14 15 -25 c0 -8 -6 -15 -15 -15z" fill="var(--pin-red)"/>
        <circle cx="104" cy="53" r="5" fill="var(--map-road)"/>
      </svg>

      <div class="store-details">
        <p class="store-details__block"><span class="store-details__label">Address</span>shop 5/214 Larkmoor Vale Rd,<br>NSW 2049</p>
        <p class="store-details__block"><span class="store-details__label">Phone</span>02 8154 3907</p>
        <p class="store-details__block"><span class="store-details__label">Opening hours</span>Mon – Fri 10:00am – 5:30pm<br>Sat – Sun 10:00am – 5:30pm</p>
      </div>
    </section>

    <div class="damask-strip damask-strip--right" role="img" aria-label="Pink damask wallpaper pattern"></div>

    <div class="model-photo" role="img" aria-label="Photograph of a model wearing a black lace corset and briefs against a dark teal and gold damask wallpaper"></div>
  </main>
</body>
</html>
```